5'x15' banner for sustainable apartments

Meadow 427 is a sustainable community that focuses on well being of tenants and reduction of carbon footprint.
Need an eye catching banner to be displayed on the side of a building. Walls are gray (see pic), so it's a perfect canvass to splash some colors. Banner shall include the word "apartments" and represent sustainability (ie. sustainable apartments).
Please check website to see more about the community: www.meadow427-living.example
Dimensions are 5' W x 15' H.
Daily traffic is approx. 20k cars.

Target Market(s)

we target environmentally conscious tenants who want to live in a community of like-minded people. We have a community garden, and reuse "gray" water for irrigation. We've also implemented recycling programs.
We've also built a deck were we have yoga practices -free of charge- for our tenants and guests.

Industry/Entity Type

Community

Font styles to use
Other font styles liked:
• Leelawadee UI

Requirements
Must have
• Should be understood that these are apartments for rent.
• whatever imagery is to be used, should have a strong association with sustainability.
• If any text, use Leelawadee UI font.
Nice to have
• well being imagery / association
• The picture with the painted mural is not from the subject building, but liked the drawing, so could spark some idea.

```html
<!DOCTYPE html>
<html lang="en">
<head>
<meta charset="utf-8">
<title>Meadow 427 – Apartments for Rent Banner</title>
<link href="https://fonts.googleapis.com/css2?family=Hind:wght@400;500;600;700&display=swap" rel="stylesheet">
<style>
  :root{
    --page:#dfe3e6;
    --band:#555756;
    --band-dark:#4a4c4b;
    --body:#eefbe7;
    --green:#8cc63f;
    --green-deep:#5fa832;
    --green-soft:#cfe9a8;
    --green-pale:#e4f5d2;
    --ink:#2f3130;
    --muted:#555a55;
    --white:#ffffff;
  }
  *{margin:0;padding:0;box-sizing:border-box}
  html,body{width:800px;height:1200px;overflow:hidden;background:var(--page)}
  body{font-family:"Hind",sans-serif;color:var(--ink)}
  .banner{position:absolute;left:200px;top:0;width:400px;height:1200px;background:var(--body);overflow:hidden}
  .backdrop{position:absolute;left:0;top:160px;width:400px;height:952px;
    background:linear-gradient(100deg,var(--green-soft) 0%,var(--green-pale) 30%,var(--body) 55%,var(--body) 100%)}
  .header{position:absolute;left:0;top:0;width:400px;height:160px;background:var(--band)}
  .brand{position:absolute;right:48px;top:24px;text-align:right;color:var(--green);font-weight:700;font-size:60px;line-height:62px;letter-spacing:1px;text-transform:uppercase}
  .apartments{position:absolute;left:0;top:205px;width:400px;font-weight:600;font-size:46px;letter-spacing:1px;color:var(--ink);text-align:center}
  .for-rent{position:absolute;left:0;top:272px;width:400px;font-weight:600;font-size:34px;color:var(--green-deep);text-align:center}
  .call-top{position:absolute;left:0;top:360px;width:400px;text-align:center;font-size:22px;color:var(--ink)}
  .call-top span{color:var(--green)}
  .tagline{position:absolute;left:70px;top:440px;width:280px;text-align:center;font-size:12.5px;line-height:16px;color:var(--muted)}
  .feature{position:absolute;left:45px;width:330px;height:100px}
  .feature .photo{position:absolute;left:0;top:0;width:96px;height:96px;border-radius:50%;border:3px solid var(--green)}
  .feature h3{position:absolute;left:115px;top:8px;font-weight:600;font-size:16px;color:var(--green);text-transform:uppercase;letter-spacing:.3px}
  .feature p{position:absolute;left:115px;top:36px;width:195px;font-size:10.5px;line-height:13px;color:var(--muted)}
  .f1{top:530px}.f1 .photo{background:radial-gradient(circle at 50% 40%,#c9a98d,#6f8a52)}
  .f2{top:645px}.f2 .photo{background:radial-gradient(circle at 50% 45%,#6fc4ea,#1e6fa8)}
  .f3{top:760px}.f3 .photo{background:radial-gradient(circle at 50% 45%,#c7b79c,#8da86a)}
  .f4{top:875px}.f4 .photo{background:radial-gradient(circle at 50% 45%,#e8e8e8,#6e6e6e)}
  .cta{position:absolute;left:0;top:1020px;width:400px;text-align:center;font-weight:600;font-size:24px;line-height:30px;color:var(--ink);text-transform:uppercase}
  .footer{position:absolute;left:0;top:1112px;width:400px;height:88px;background:var(--band)}
  .footer .call{position:absolute;left:0;top:10px;width:400px;text-align:center;font-size:21px;color:var(--white)}
  .footer .call span{color:var(--green)}
  .footer .social{position:absolute;left:0;top:48px;width:400px;height:40px;background:var(--band-dark);display:flex;align-items:center;justify-content:center;gap:14px;color:var(--white);font-size:21px;text-transform:uppercase}
  .footer .dot{width:30px;height:30px;border-radius:50%;background:var(--green)}
</style>
</head>
<body>
<main class="banner">
  <div class="backdrop" role="img" aria-label="Decorative background of sweeping green curves and soft bokeh circles"></div>

  <header class="header">
    <div class="brand">Meadow<br>427</div>
  </header>

  <h1 class="apartments">APARTMENTS</h1>
  <h2 class="for-rent">FOR RENT</h2>
  <p class="call-top">CALL: <span>XXX XXX XXX</span></p>
  <p class="tagline">A community of people for people that want a Sustainable lifestyle.</p>

  <section class="feature f1">
    <div class="photo" role="img" aria-label="Photo of a smiling gardener holding fresh vegetables"></div>
    <h3>Community Garden</h3>
    <p>Grow your own vegetables, eat fresh and clean and save money!</p>
  </section>
  <section class="feature f2">
    <div class="photo" role="img" aria-label="Photo of a child swimming underwater in the pool"></div>
    <h3>Pool &amp; BBQ</h3>
    <p>Dive into our new 7ft pool, and see what you can cook up with our BBQ.</p>
  </section>
  <section class="feature f3">
    <div class="photo" role="img" aria-label="Photo of a woman holding a yoga mat outdoors"></div>
    <h3>Yoga Classes</h3>
    <p>Its proven that yoga improves your quality of living. Tenants get free sessions!</p>
  </section>
  <section class="feature f4">
    <div class="photo" role="img" aria-label="Photo of a man carrying a bicycle"></div>
    <h3>Bike Storage</h3>
    <p>Eliminate emmisions, by making use of our secure personal bike racks!</p>
  </section>

  <p class="cta">We offer much more,<br>book your tour !</p>

  <footer class="footer">
    <p class="call"><span>CALL:</span> XXX XXX XXX</p>
    <div class="social"><span class="dot"></span><span>Meadow 427</span></div>
  </footer>
</main>
</body>
</html>
```